Copper Ridge Hitters Baseball Club (CRH)

Looking for a new web page for Middle School/High School focused baseball club that works with elite prospects. This site will introduce our program to the Northern Virginia area. We will need the ability to sell merchandise and 4+ Services

We would like to use a color theme that goes with our label attached.

We also already own the CRH-VX.com

Industry/Entity Type

Sports Baseball

Coding

Coded - Design and coding required

Number of Pages Required

5+ page

Colors
0054AA
0677BA
7BADD7
CADEEF
E8F1F8

Requirements
Must have
• Ability to upload photos. Page for player profiles/Program Description/Game stats and standings
Nice to have
• pinelakeprospectsball.com otterballclub.net quarrygritballclub.com

```html
<!DOCTYPE html>
<html lang="en">
<head>
<meta charset="utf-8">
<title>Copper Ridge Hitters Baseball Club – Home Page Concepts</title>
<link href="https://fonts.googleapis.com/css2?family=Quicksand:wght@500;700&family=Lato:wght@400;700&display=swap" rel="stylesheet">
<style>
:root{
  --board:#8a8a8a;
  --orange:#e8431f;
  --orange-soft:#f07a5a;
  --navy:#0b1442;
  --navy-deep:#070b2c;
  --blue:#123f7a;
  --teal:#17809a;
  --teal-dark:#0d5568;
  --green:#6b8a1f;
  --ink:#1b2235;
  --text:#3b3f4a;
  --white:#ffffff;
  --black:#050505;
  --row:#0f1a22;
  --row-alt:#14232c;
}
*{box-sizing:border-box;margin:0;padding:0}
html,body{width:750px;height:1200px;overflow:hidden}
body{background:var(--board);position:relative;font-family:"Lato",sans-serif;color:var(--text)}
.page{position:absolute;top:38px;background:var(--white);transform:scale(.496);transform-origin:0 0;overflow:hidden}
.page--flat{left:36px;width:640px}
.page--curved{left:385px;width:663px}
.h{font-family:"Quicksand",sans-serif;font-weight:700}

/* top bar */
.topbar{height:23px;background:var(--orange);color:var(--white);font-size:7.5px;display:flex;align-items:center;justify-content:space-between;padding:0 60px}
.topbar__right{display:flex;gap:14px;align-items:center}
.dots{display:flex;gap:4px}
.dots i{display:block;width:6px;height:6px;border-radius:50%;background:var(--white)}

/* hero */
.hero{position:relative;height:347px;color:var(--white);overflow:hidden}
.page--curved .hero{height:370px}
.hero__photo{position:absolute;inset:0;background:
  radial-gradient(ellipse 40% 55% at 72% 45%,#2c6fa8 0%,transparent 70%),
  radial-gradient(ellipse 60% 20% at 40% 72%,#c9693e 0%,transparent 80%),
  linear-gradient(180deg,#0a0f45 0%,#17307a 45%,#2a3e6e 68%,#7a4a33 86%,#a8583a 100%)}
.nav{position:relative;display:flex;align-items:center;justify-content:space-between;padding:14px 60px 0}
.brand{display:flex;align-items:center;gap:6px;font-family:"Quicksand",sans-serif;font-weight:700;color:var(--white);font-size:20px}
.brand__dot{width:10px;height:10px;border-radius:50%;background:var(--orange)}
.nav__links{display:flex;gap:17px;font-size:7.5px}
.hero__copy{position:relative;padding:60px 0 0 58px;width:330px}
.hero__title{font-size:21px;line-height:28px;letter-spacing:.5px}
.hero__lede{font-size:7.5px;line-height:10px;margin-top:10px}
.btn{display:inline-flex;align-items:center;gap:12px;margin-top:18px;padding:0 8px;height:24px;background:var(--navy);color:var(--white);font-size:7.5px;border:1.5px solid var(--orange);border-top:none;border-left:none}
.btn__ball{width:13px;height:13px;border-radius:50%;background:var(--white);border:1.5px solid #d23}
.hero__curve{position:absolute;left:0;bottom:0;width:100%;height:70px}

/* about */
.about{height:277px;display:flex;align-items:center;padding:0 60px 0 52px;gap:30px}
.crest{width:240px;height:190px;display:flex;align-items:center;justify-content:center;gap:10px;font-family:"Quicksand",sans-serif;font-weight:700;font-size:54px;color:var(--navy)}
.crest__dot{width:22px;height:22px;border-radius:50%;background:var(--orange)}
.about__body{flex:1}
.about__title{font-size:15px;line-height:22px;color:var(--navy)}
.about__title span{color:var(--orange)}
.about__text{font-size:7.3px;line-height:13.6px;margin-top:12px;color:var(--ink)}

/* player */
.player{position:relative;height:343px;background:linear-gradient(180deg,#135f7a 0%,#17809a 55%,#1a8aa0 100%);overflow:hidden}
.page--curved .player{height:355px}
.player__photo{position:absolute;left:95px;top:14px;width:110px;height:312px;border-radius:40px 40px 10px 10px;background:linear-gradient(180deg,#2a4656 0%,#16303c 60%,#0e202a 100%);opacity:.85}
.player__info{position:absolute;left:248px;top:40px;width:300px}
.player__head{display:flex;align-items:center;gap:32px}
.player__name{font-size:17px;color:var(--white)}
.mini-brand{font-family:"Quicksand",sans-serif;font-weight:700;font-size:16px;color:var(--white)}
.pills{display:flex;gap:10px;margin-top:28px}
.pill{background:var(--white);font-family:"Quicksand",sans-serif;font-weight:700;font-size:10px;color:var(--navy);height:24px;padding:0 10px;display:flex;align-items:center;gap:8px}
.pill span{color:var(--orange)}
.cards{display:flex;gap:19px;margin-top:20px}
.stat-card{width:139px;background:var(--white);padding:10px 10px 12px}
.stat-card h4{font-size:10.5px;color:var(--navy);margin-bottom:4px}
.stat-card li{list-style:none;font-size:10px;color:var(--ink);padding:4px 8px;border-bottom:1px solid #ddd}
.stat-card li:last-child{border-bottom:none}
.stat-card li span{color:var(--orange)}

/* services */
.services{height:291px;text-align:center;padding-top:50px}
.page--curved .services{height:295px}
.section-title{font-size:17px;color:var(--ink)}
.services__grid{display:flex;justify-content:center;gap:14px;margin-top:28px}
.service{width:120px;height:136px;text-align:left;color:var(--white);padding:10px 20px}
.page--curved .service{width:124px;height:141px}
.service--navy{background:linear-gradient(160deg,#0e3876,#17306a)}
.service--orange{background:linear-gradient(160deg,#e05a34,#c8482a)}
.service--blue{background:linear-gradient(160deg,#1a4f86,#163e6c)}
.service--green{background:linear-gradient(160deg,#7a9a28,#587a1a)}
.service__num{font-family:"Quicksand",sans-serif;font-weight:700;font-size:24px;line-height:28px}
.service__title{font-size:10.5px}
.service__text{font-size:7.3px;line-height:13.6px;margin-top:4px;opacity:.85}
.service__link{font-size:7.5px;font-weight:700;margin-top:2px}

/* standings */
.standings{height:385px;text-align:center;padding-top:36px;background:linear-gradient(180deg,#1d7d93 0%,#2296ab 40%,#2b6f80 75%,#334f58 100%)}
.page--curved .standings{height:399px}
.standings .section-title{color:var(--white)}
.table{width:404px;margin:18px auto 0;border-radius:8px;overflow:hidden;background:var(--row);border-collapse:collapse;font-family:"Quicksand",sans-serif;font-weight:700;font-size:9px;color:var(--white)}
.page--curved .table{width:418px}
.table th{background:var(--orange);height:22px;font-weight:700;text-align:left;padding:0 6px}
.table td{height:24.5px;padding:0 6px;text-align:left}
.table tr:nth-child(even) td{background:var(--row-alt)}
.team{display:flex;align-items:center;gap:12px}
.team i{display:block;width:12px;height:12px;border-radius:50%;background:#9aa4ad}
.table th:first-child,.table td:first-child{padding-left:22px}

/* testimonials */
.testimonials{position:relative;height:276px;text-align:center;padding-top:44px}
.page--curved .testimonials{height:284px}
.testi{position:relative;margin-top:22px;height:150px}
.testi__band{position:absolute;left:60px;top:44px;width:252px;height:58px;background:var(--orange-soft)}
.page--curved .testi__band{background:var(--orange)}
.testi__photo{position:absolute;left:101px;top:0;width:169px;height:148px;background:linear-gradient(180deg,#e4e4e2,#cfd2d6)}
.testi__body{position:absolute;left:340px;top:18px;width:240px;text-align:left}
.testi__quote{font-family:"Quicksand",sans-serif;font-weight:700;color:var(--orange);font-size:22px;line-height:14px}
.testi__text{font-size:7.3px;line-height:13.6px;margin-top:4px;color:var(--text)}
.testi__meta{display:flex;gap:50px;align-items:center;margin-top:8px;font-size:7.5px;color:var(--ink)}
.stars{color:#f0a11c;letter-spacing:1px;font-size:8px}

/* footer */
.footer{position:relative;height:198px;background:var(--black);color:var(--white);padding:24px 60px 0}
.page--curved .footer{height:262px;padding-top:78px;background:transparent}
.footer__bg{position:absolute;left:0;top:0;width:100%;height:100%}
.footer__cols{position:relative;display:flex}
.footer__brand{width:143px;font-family:"Quicksand",sans-serif;font-weight:700;font-size:30px;display:flex;align-items:center;gap:8px;height:100px}
.footer__brand i{display:block;width:12px;height:12px;border-radius:50%;background:var(--orange)}
.footer__col{width:124px}
.footer__col--help{width:96px}
.footer__col h5{font-size:9px;margin-bottom:8px}
.footer__col li{list-style:none;font-size:7.3px;line-height:16px}
.subscribe{display:flex;margin-top:4px}
.subscribe__field{width:124px;height:21px;background:var(--white);color:#333;font-size:7.3px;display:flex;align-items:center;padding-left:10px}
.subscribe__send{width:33px;height:21px;background:var(--orange)}
.footer .dots{margin-top:10px;gap:8px}
.footer__legal{position:absolute;left:60px;right:60px;bottom:12px;border-top:1px solid #222;padding-top:12px;text-align:center;font-size:7.3px}
</style>
</head>
<body>

<!-- Concept A -->
<div class="page page--flat">
  <div class="topbar"><span>Lorem ipsum dolor sit amet, consectetur adipiscing elit</span><div class="topbar__right"><div class="dots"><i></i><i></i><i></i></div><span>Contact Us | Login</span></div></div>
  <header class="hero">
    <div class="hero__photo" role="img" aria-label="Catcher lunging for a ball in a floodlit stadium at dusk"></div>
    <nav class="nav"><div class="brand"><i class="brand__dot"></i>CRH</div><div class="nav__links"><span>Home</span><span>About Us</span><span>Player profiles</span><span>Program Description</span><span>Game stats and standings</span><span>Our News</span></div></nav>
    <div class="hero__copy">
      <h1 class="hero__title h">COPPER RIDGE HITTERS BASEBALL CLUB</h1>
      <p class="hero__lede">The CRHBC is the first team in the DMV that will be selecting players from it's tryout pool that show promise</p>
      <span class="btn">Learn More <i class="btn__ball"></i></span>
    </div>
  </header>
  <section class="about">
    <div class="crest"><i class="crest__dot"></i>CRH</div>
    <div class="about__body">
      <h2 class="about__title h">ABOUT THE <span>COPPER RIDGE HITTERS</span> BASEBALL CLUB</h2>
      <p class="about__text">The CRHBC is the first team in the DMV that will be selecting players from it's tryout pool that show promise in OVERALL athletic ability and PLATE AGRESSIVENESS. Our tryouts will consist of 1) a comprehensive assessment of speed, power, balance, mobility and baseball SPECIFIC movement (the Copper Ridge Combine), and 2) a data-driven assessment of plate discipline, aggressiveness, and launch metrics; the cutting edge of baseball testing ability.</p>
      <span class="btn">Learn More <i class="btn__ball"></i></span>
    </div>
  </section>
  <section class="player">
    <div class="player__photo" role="img" aria-label="Batter in dark uniform ready to swing"></div>
    <div class="player__info">
      <div class="player__head"><h3 class="player__name h">Rowan Castellano</h3><span class="mini-brand">CRH</span></div>
      <div class="pills"><div class="pill">AGE <span>25</span></div><div class="pill">HEIGHT <span>1.82M</span></div><div class="pill">WEIGHT <span>81KG</span></div></div>
      <div class="cards">
        <div class="stat-card"><h4 class="h">Player Profiles</h4><ul><li><span>(R)</span> Bats</li><li><span>(R)</span> Throws</li><li><span>(75)</span> Fastball</li><li><span>(N/A)</span> Slider</li></ul></div>
        <div class="stat-card"><h4 class="h">Game Standings</h4><ul><li><span>(19)</span> Appearances</li><li><span>(7.7)</span> 60 yard</li><li><span>(N/A)</span> OF Velo</li><li><span>(N/A)</span> Bat Speed</li></ul></div>
      </div>
    </div>
  </section>
  <section class="services">
    <h2 class="section-title h">Our Services</h2>
    <div class="services__grid">
      <div class="service service--navy"><div class="service__num">01</div><div class="service__title h">Lorem Ipsum</div><p class="service__text">Lorem ipsum dolor sit amet, consectetur adipiscing elit, sed do eiusmod tempor.</p><div class="service__link">Learn More</div></div>
      <div class="service service--orange"><div class="service__num">02</div><div class="service__title h">Lorem Ipsum</div><p class="service__text">Lorem ipsum dolor sit amet, consectetur adipiscing elit, sed do eiusmod tempor.</p><div class="service__link">Learn More</div></div>
      <div class="service service--blue"><div class="service__num">03</div><div class="service__title h">Lorem Ipsum</div><p class="service__text">Lorem ipsum dolor sit amet, consectetur adipiscing elit, sed do eiusmod tempor.</p><div class="service__link">Learn More</div></div>
      <div class="service service--green"><div class="service__num">04</div><div class="service__title h">Lorem Ipsum</div><p class="service__text">Lorem ipsum dolor sit amet, consectetur adipiscing elit, sed do eiusmod tempor.</p><div class="service__link">Learn More</div></div>
    </div>
  </section>
  <section class="standings" role="img" aria-label="Blurred baseball infield dirt behind the standings table">
    <h2 class="section-title h">Game Standings</h2>
    <table class="table">
      <tr><th style="width:55%">Team</th><th>W</th><th>L</th><th>Pts</th><th>%</th></tr>
      <tr><td><div class="team"><i></i>Rowan Castellano</div></td><td>14</td><td>1</td><td>24</td><td>93</td></tr>
      <tr><td><div class="team"><i></i>Rowan Castellano</div></td><td>14</td><td>1</td><td>24</td><td>93</td></tr>
      <tr><td><div class="team"><i></i>Rowan Castellano</div></td><td>14</td><td>1</td><td>24</td><td>93</td></tr>
      <tr><td><div class="team"><i></i>Rowan Castellano</div></td><td>14</td><td>1</td><td>24</td><td>93</td></tr>
      <tr><td><div class="team"><i></i>Rowan Castellano</div></td><td>14</td><td>1</td><td>24</td><td>93</td></tr>
      <tr><td><div class="team"><i></i>Rowan Castellano</div></td><td>14</td><td>1</td><td>24</td><td>93</td></tr>
      <tr><td><div class="team"><i></i>Rowan Castellano</div></td><td>14</td><td>1</td><td>24</td><td>93</td></tr>
      <tr><td><div class="team"><i></i>Rowan Castellano</div></td><td>14</td><td>1</td><td>24</td><td>93</td></tr>
      <tr><td><div class="team"><i></i>Rowan Castellano</div></td><td>14</td><td>1</td><td>24</td><td>93</td></tr>
      <tr><td><div class="team"><i></i>Rowan Castellano</div></td><td>14</td><td>1</td><td>24</td><td>93</td></tr>
    </table>
  </section>
  <section class="testimonials">
    <h2 class="section-title h">Client Testimonials</h2>
    <div class="testi">
      <div class="testi__band"></div>
      <div class="testi__photo" role="img" aria-label="Portrait of a smiling client"></div>
      <div class="testi__body">
        <div class="testi__quote">“</div>
        <p class="testi__text">Lorem ipsum dolor sit amet, consectetur adipiscing elit, sed do eiusmod tempor incididunt ut labore et dolore magna aliqua. Quis ipsum suspendisse ultrices gravida. Risus commodo viverra maecenas accumsan lacus vel facilisis. Lorem ipsum dolor sit amet, consectetur adipiscing elit, sed do eiusmod tempor incididunt ut labore et dolore magna aliqua.</p>
        <div class="testi__meta"><span class="stars">★★★★★</span><span>— Rowan Castellano</span></div>
      </div>
    </div>
  </section>
  <footer class="footer">
    <div class="footer__cols">
      <div class="footer__brand"><i></i>CRH</div>
      <div class="footer__col"><h5 class="h">Quick Link</h5><ul><li>Home</li><li>About Us</li><li>Player profiles</li><li>Program Description</li><li>Game stats and standings</li><li>Our News</li></ul></div>
      <div class="footer__col footer__col--help"><h5 class="h">Help Link</h5><ul><li>Support / Contact</li><li>Privacy Policies</li><li>Terms of use</li><li>Service &amp; Support</li></ul></div>
      <div><h5 class="h" style="font-size:9px">Subscribe To Our Newsletter</h5><div class="subscribe"><div class="subscribe__field">Enter Your Email</div><div class="subscribe__send"></div></div><div class="dots"><i></i><i></i><i></i><i></i></div></div>
    </div>
    <div class="footer__legal">© Copyrights 2021 Company Name &nbsp;|&nbsp; All Rights Reserved</div>
  </footer>
</div>

<!-- Concept B -->
<div class="page page--curved">
  <div class="topbar"><span>Lorem ipsum dolor sit amet, consectetur adipiscing elit</span><div class="topbar__right"><div class="dots"><i></i><i></i><i></i></div><span>Contact Us | Login</span></div></div>
  <header class="hero">
    <div class="hero__photo" role="img" aria-label="Catcher lunging for a ball in a floodlit stadium at dusk"></div>
    <nav class="nav"><div class="brand"><i class="brand__dot"></i>CRH</div><div class="nav__links"><span>Home</span><span>About Us</span><span>Player profiles</span><span>Program Description</span><span>Game stats and standings</span><span>Our News</span></div></nav>
    <div class="hero__copy" style="width:360px">
      <h1 class="hero__title h">COPPER RIDGE HITTERS BASEBALL CLUB</h1>
      <p class="hero__lede">The CRHBC is the first team in the DMV that will be selecting players from it's tryout pool that show promise</p>
      <span class="btn">Learn More <i class="btn__ball"></i></span>
    </div>
    <svg class="hero__curve" viewBox="0 0 663 70" preserveAspectRatio="none" aria-hidden="true">
      <path d="M0 10 Q330 90 663 0 L663 70 L0 70Z" fill="#ffffff"/>
      <path d="M0 10 Q300 85 640 20 Q330 70 0 26Z" fill="#e8431f"/>
    </svg>
  </header>
  <section class="about">
    <div class="crest"><i class="crest__dot"></i>CRH</div>
    <div class="about__body">
      <h2 class="about__title h">ABOUT THE <span>COPPER RIDGE HITTERS</span> BASEBALL CLUB</h2>
      <p class="about__text">The CRHBC is the first team in the DMV that will be selecting players from it's tryout pool that show promise in OVERALL athletic ability and PLATE AGRESSIVENESS. Our tryouts will consist of 1) a comprehensive assessment of speed, power, balance, mobility and baseball SPECIFIC movement (the Copper Ridge Combine), and 2) a data-driven assessment of plate discipline, aggressiveness, and launch metrics; the cutting edge of baseball testing ability.</p>
      <span class="btn">Learn More <i class="btn__ball"></i></span>
    </div>
  </section>
  <section class="player">
    <div class="player__photo" style="left:110px;top:18px;height:318px" role="img" aria-label="Batter in dark uniform ready to swing"></div>
    <div class="player__info" style="left:258px;top:44px">
      <div class="player__head"><h3 class="player__name h">Rowan Castellano</h3><span class="mini-brand">CRH</span></div>
      <div class="pills"><div class="pill">AGE <span>25</span></div><div class="pill">HEIGHT <span>1.82M</span></div><div class="pill">WEIGHT <span>81KG</span></div></div>
      <div class="cards">
        <div class="stat-card" style="width:143px"><h4 class="h">Player Profiles</h4><ul><li><span>(R)</span> Bats</li><li><span>(R)</span> Throws</li><li><span>(75)</span> Fastball</li><li><span>(N/A)</span> Slider</li></ul></div>
        <div class="stat-card" style="width:143px"><h4 class="h">Game Standings</h4><ul><li><span>(19)</span> Appearances</li><li><span>(7.7)</span> 60 yard</li><li><span>(N/A)</span> OF Velo</li><li><span>(N/A)</span> Bat Speed</li></ul></div>
      </div>
    </div>
  </section>
  <section class="services">
    <h2 class="section-title h">Our Services</h2>
    <div class="services__grid">
      <div class="service service--navy"><div class="service__num">01</div><div class="service__title h">Lorem Ipsum</div><p class="service__text">Lorem ipsum dolor sit amet, consectetur adipiscing elit, sed do eiusmod tempor.</p><div class="service__link">Learn More</div></div>
      <div class="service service--orange"><div class="service__num">02</div><div class="service__title h">Lorem Ipsum</div><p class="service__text">Lorem ipsum dolor sit amet, consectetur adipiscing elit, sed do eiusmod tempor.</p><div class="service__link">Learn More</div></div>
      <div class="service service--blue"><div class="service__num">03</div><div class="service__title h">Lorem Ipsum</div><p class="service__text">Lorem ipsum dolor sit amet, consectetur adipiscing elit, sed do eiusmod tempor.</p><div class="service__link">Learn More</div></div>
      <div class="service service--green"><div class="service__num">04</div><div class="service__title h">Lorem Ipsum</div><p class="service__text">Lorem ipsum dolor sit amet, consectetur adipiscing elit, sed do eiusmod tempor.</p><div class="service__link">Learn More</div></div>
    </div>
  </section>
  <section class="standings" role="img" aria-label="Blurred baseball infield dirt behind the standings table">
    <h2 class="section-title h">Game Standings</h2>
    <table class="table">
      <tr><th style="width:55%">Team</th><th>W</th><th>L</th><th>Pts</th><th>%</th></tr>
      <tr><td><div class="team"><i></i>Rowan Castellano</div></td><td>14</td><td>1</td><td>24</td><td>93</td></tr>
      <tr><td><div class="team"><i></i>Rowan Castellano</div></td><td>14</td><td>1</td><td>24</td><td>93</td></tr>
      <tr><td><div class="team"><i></i>Rowan Castellano</div></td><td>14</td><td>1</td><td>24</td><td>93</td></tr>
      <tr><td><div class="team"><i></i>Rowan Castellano</div></td><td>14</td><td>1</td><td>24</td><td>93</td></tr>
      <tr><td><div class="team"><i></i>Rowan Castellano</div></td><td>14</td><td>1</td><td>24</td><td>93</td></tr>
      <tr><td><div class="team"><i></i>Rowan Castellano</div></td><td>14</td><td>1</td><td>24</td><td>93</td></tr>
      <tr><td><div class="team"><i></i>Rowan Castellano</div></td><td>14</td><td>1</td><td>24</td><td>93</td></tr>
      <tr><td><div class="team"><i></i>Rowan Castellano</div></td><td>14</td><td>1</td><td>24</td><td>93</td></tr>
      <tr><td><div class="team"><i></i>Rowan Castellano</div></td><td>14</td><td>1</td><td>24</td><td>93</td></tr>
      <tr><td><div class="team"><i></i>Rowan Castellano</div></td><td>14</td><td>1</td><td>24</td><td>93</td></tr>
    </table>
  </section>
  <section class="testimonials">
    <h2 class="section-title h">Client Testimonials</h2>
    <div class="testi">
      <div class="testi__band" style="width:262px"></div>
      <div class="testi__photo" style="left:105px;width:175px;height:154px" role="img" aria-label="Portrait of a smiling client"></div>
      <div class="testi__body" style="left:352px;width:250px">
        <div class="testi__quote">“</div>
        <p class="testi__text">Lorem ipsum dolor sit amet, consectetur adipiscing elit, sed do eiusmod tempor incididunt ut labore et dolore magna aliqua. Quis ipsum suspendisse ultrices gravida. Risus commodo viverra maecenas accumsan lacus vel facilisis. Lorem ipsum dolor sit amet, consectetur adipiscing elit, sed do eiusmod tempor incididunt ut labore et dolore magna aliqua.</p>
        <div class="testi__meta"><span class="stars">★★★★★</span><span>— Rowan Castellano</span></div>
      </div>
    </div>
  </section>
  <footer class="footer">
    <svg class="footer__bg" viewBox="0 0 663 262" preserveAspectRatio="none" aria-hidden="true">
      <path d="M0 60 Q330 -20 663 60 L663 262 L0 262Z" fill="#050505"/>
      <path d="M30 40 Q360 -10 663 46 L663 58 Q360 0 30 40Z" fill="#e8431f"/>
    </svg>
    <div class="footer__cols">
      <div class="footer__brand" style="width:150px"><i></i>CRH</div>
      <div class="footer__col" style="width:128px"><h5 class="h">Quick Link</h5><ul><li>Home</li><li>About Us</li><li>Player profiles</li><li>Program Description</li><li>Game stats and standings</li><li>Our News</li></ul></div>
      <div class="footer__col footer__col--help" style="width:100px"><h5 class="h">Help Link</h5><ul><li>Support / Contact</li><li>Privacy Policies</li><li>Terms of use</li><li>Service &amp; Support</li></ul></div>
      <div><h5 class="h" style="font-size:9px">Subscribe To Our Newsletter</h5><div class="subscribe"><div class="subscribe__field" style="width:128px">Enter Your Email</div><div class="subscribe__send"></div></div><div class="dots"><i></i><i></i><i></i><i></i></div></div>
    </div>
    <div class="footer__legal">© Copyrights 2021 Company Name &nbsp;|&nbsp; All Rights Reserved</div>
  </footer>
</div>

</body>
</html>
```